Finance web application design

We need a design for a new responsive finance web application. It should look uber professional and modern.

Inspiration and design we like:

website:
http://www.brennickhale.com/

The application presented here:
http://markets.pelvantgrid.com/en/products/tools-applications/trading-investment-tools/zarvo-trading-software.html

https://apps.quillstore.example/us/app/ferncastle-for-tablet/id582917463?mt=8

The application presented here (Slatepad version):
https://apps.quillstore.example/en/app/trevik-forex-trading/id649205318?mt=8&utm_source=trevikButton

Target Market(s)

Private Investors

Industry/Entity Type

Finance

Number of Pages Required

5+ page

Font styles to use
Other font styles liked:
• Nobile

Requirements
Must have
• Colors for "up" changes: green
• Colors for "down" changes: red
• Fonts in tables must be very easy to read -
• Deliver design for all pages attached.
Nice to have
• A dark (gray) background
• Graphs should be shaded and partly transparent - orange or blue
• White text as "normal" - orange text / blue text for headers
Should not have
• White background

```html
<!DOCTYPE html>
<html lang="en">
<head>
<meta charset="utf-8">
<title>Ledgerwise – NRX Index</title>
<link href="https://fonts.googleapis.com/css2?family=Open+Sans:wght@400;600;700&display=swap" rel="stylesheet">
<style>
:root{
  --page:#2a2c30;
  --surface:#33363b;
  --surface-2:#2e3135;
  --ink:#eceef0;
  --muted:#b3b7bc;
  --soft:#8d9298;
  --line:#4a4e54;
  --nav-bg:#212326;
  --nav-ink:#c4c7cb;
  --bar:#dc962c;
  --accent:#e59a2c;
  --accent-dark:#c47f1c;
  --blue:#3d9ad9;
  --up:#43c163;
  --chip:#43474d;
  --table-head:#1e2023;
  --field:#26282b;
}
*{box-sizing:border-box;margin:0;padding:0}
html,body{width:1200px;height:1125px;overflow:hidden;background:var(--page)}
body{font-family:"Open Sans",Arial,sans-serif;color:var(--ink)}
.stage{position:relative;width:1170px;height:1097px;transform:scale(1.02564);transform-origin:0 0}
.abs{position:absolute}

.topnav{left:0;top:0;width:1170px;height:71px;background:var(--nav-bg);border-bottom:4px solid var(--bar)}
.topnav .item{position:absolute;top:0;height:67px;line-height:70px;font-size:14px;color:var(--nav-ink);text-align:center;border-right:1px solid var(--line);letter-spacing:.2px}
.fund-search{left:877px;top:19px;width:194px;height:31px;border:1px solid var(--line);background:var(--field);border-radius:2px;font-size:12px;color:var(--soft);padding:7px 11px}
.fund-search svg{position:absolute;right:9px;top:8px}
.signout{left:1080px;top:19px;width:74px;height:30px;background:var(--accent);border:1px solid var(--accent-dark);border-radius:3px;font-size:13px;color:#222;text-align:center;line-height:28px}

.brand{left:15px;top:88px;display:flex;align-items:center;gap:8px}
.brand .mark{width:14px;height:14px;background:var(--accent)}
.brand .name{font-size:32px;font-weight:700;color:var(--accent);letter-spacing:-.5px;line-height:44px}

.rule{left:15px;width:1140px;height:1px;background:var(--line)}

.title-row{left:15px;top:156px;display:flex;align-items:baseline;gap:12px}
.title-row h1{font-size:26px;font-weight:700;color:var(--ink)}
.title-row .change{font-size:14px;font-weight:600;color:var(--up)}
.title-row svg{align-self:center;margin-right:-2px}

.panel{border:1px solid var(--line);background:var(--surface)}
.ranges{left:32px;top:247px;display:flex;gap:4px}
.ranges span{width:62px;height:33px;background:var(--chip);font-size:14px;text-align:center;line-height:33px;color:var(--ink)}
.plot{left:32px;top:295px;width:370px;height:290px;background:var(--surface-2)}

.panel-title{font-size:19px;font-weight:400;color:var(--accent)}
.select{height:33px;border:1px solid var(--line);font-size:12px;color:var(--muted);padding:8px 11px;background:var(--field)}
.select::after{content:"";position:absolute;right:9px;top:13px;border-left:6px solid transparent;border-right:6px solid transparent;border-top:7px solid var(--soft)}
.text-input{height:33px;border:1px solid var(--line);font-size:12px;color:var(--soft);padding:8px 11px;background:var(--field)}

.section-head{font-size:18px;font-weight:700;color:var(--accent)}
.about{left:16px;top:658px;width:555px;font-size:13px;line-height:20px;color:var(--muted)}

.card-row{border-top:1px solid var(--line)}
.small{font-size:11px;color:var(--ink)}
.tiny{font-size:9px;color:var(--soft)}
.card-head{font-size:18px;color:var(--accent)}

.perf{left:595px;top:667px;width:221px;border-collapse:collapse;font-size:13px;color:var(--ink);background:var(--surface)}
.perf th{height:35px;background:var(--table-head);border-right:1px solid var(--line)}
.perf td{height:40.8px;border:1px solid var(--line);text-align:center;width:50%}
.perf td:first-child{text-align:right;padding-right:40px}
.perf td:last-child{text-align:left;padding-left:30px;color:var(--up);font-weight:600}

.footer{left:0;top:1063px;width:1170px;text-align:center;font-size:13px;color:var(--muted);word-spacing:2px}
</style>
</head>
<body>
<div class="stage">

  <nav class="topnav abs">
    <div class="item" style="left:0;width:157px">DASHBOARD</div>
    <div class="item" style="left:157px;width:137px">STRATEGIES</div>
    <div class="item" style="left:294px;width:136px">PORTFOLIOS</div>
    <div class="item" style="left:430px;width:156px">MARKET DATA</div>
    <div class="item" style="left:586px;width:126px">CUST INST.</div>
    <div class="item" style="left:712px;width:91px">USERS</div>
  </nav>
  <div class="fund-search abs">Search for funds
    <svg width="13" height="13" viewBox="0 0 13 13"><circle cx="5.5" cy="5.5" r="4.3" fill="none" stroke="#8d9298" stroke-width="1.6"/><line x1="8.6" y1="8.6" x2="12" y2="12" stroke="#8d9298" stroke-width="1.8"/></svg>
  </div>
  <div class="signout abs">Sign out</div>

  <div class="brand abs"><span class="mark"></span><span class="name">Ledgerwise</span></div>
  <div class="rule abs" style="top:149px"></div>

  <div class="title-row abs">
    <svg width="22" height="22" viewBox="0 0 24 24"><path d="M12 2.5l2.9 6.3 6.8.7-5.1 4.6 1.5 6.8L12 17.4l-6.1 3.5 1.5-6.8L2.3 9.5l6.8-.7z" fill="none" stroke="#eceef0" stroke-width="1.6" stroke-linejoin="round"/></svg>
    <h1>NRX Index - 601,45</h1>
    <span class="change">0,42 (+1,29%)</span>
  </div>
  <div class="rule abs" style="top:199px"></div>

  <section class="panel abs" style="left:14px;top:229px;width:560px;height:374px"></section>
  <div class="ranges abs"><span>1M</span><span>6M</span><span>YTD</span><span>1Y</span><span>3Y</span><span>5Y</span><span>Max</span></div>
  <div class="plot abs">
    <svg width="370" height="290" viewBox="32 295 370 290" font-family="Open Sans, Arial, sans-serif">
      <text x="217" y="338" font-size="15" fill="#eceef0" text-anchor="middle">Revenue</text>
      <g stroke="#575b62" stroke-dasharray="3 3" stroke-width="1">
        <line x1="92" y1="360" x2="368" y2="360"/><line x1="92" y1="395" x2="368" y2="395"/>
        <line x1="92" y1="430" x2="368" y2="430"/><line x1="92" y1="465" x2="368" y2="465"/>
        <line x1="92" y1="500" x2="368" y2="500"/><line x1="92" y1="535" x2="368" y2="535"/>
      </g>
      <g font-size="9" fill="#b3b7bc" text-anchor="end">
        <text x="80" y="363">10k</text><text x="80" y="398">8k</text><text x="80" y="433">6k</text>
        <text x="80" y="468">4k</text><text x="80" y="503">2k</text><text x="80" y="538">0</text>
      </g>
      <g font-size="10" fill="#b3b7bc" text-anchor="middle">
        <text x="135" y="560">Nulla</text><text x="204" y="560">Proin</text><text x="275" y="560">Fusce</text><text x="344" y="560">Sed</text>
      </g>
      <polygon points="95,430 145,401 193,424 244,406 294,425 340,357 340,535 95,535" fill="#3d9ad9" fill-opacity=".22"/>
      <polyline points="95,430 145,401 193,424 244,406 294,425 340,357" fill="none" stroke="#3d9ad9" stroke-width="3" stroke-linejoin="round"/>
      <polygon points="95,449 145,381 193,402 244,366 294,404 340,387 340,535 95,535" fill="#e59a2c" fill-opacity=".3"/>
      <polyline points="95,449 145,381 193,402 244,366 294,404 340,387" fill="none" stroke="#e59a2c" stroke-width="3.5" stroke-linejoin="round"/>
    </svg>
  </div>

  <section class="panel abs" style="left:595px;top:229px;width:340px;height:374px"></section>
  <h2 class="panel-title abs" style="left:615px;top:238px">Indicators</h2>
  <div class="select abs" style="left:614px;top:277px;width:151px">Moving Average</div>
  <div class="select abs" style="left:776px;top:277px;width:71px">50</div>
  <div class="select abs" style="left:614px;top:322px;width:151px">Moving Average</div>
  <div class="select abs" style="left:776px;top:322px;width:71px">200</div>
  <h2 class="panel-title abs" style="left:615px;top:378px">Compare</h2>
  <div class="text-input abs" style="left:614px;top:417px;width:301px">Search for instrument by name or it</div>

  <h2 class="section-head abs" style="left:14px;top:630px">Fund Details</h2>
  <p class="about abs">Fusce non neque a eros eleifend eleifend. Sed eu lobortis diam. Quisque dolor orci, ornare nec fermentum at, elementum eget nisi. Proin lectus felis, maximus at dolor et, convallis iaculis quam. Donec massa neque, imperdiet ac viverra sed, bibendum in tortor. Aliquam quis tortor dolor. Pellentesque porttitor, libero quis tempor mollis.</p>

  <section class="panel abs" style="left:14px;top:766px;width:270px;height:264px">
    <div class="abs" style="left:15px;top:14px;font-size:14px">ISIN</div>
    <div class="abs" style="right:15px;top:14px;font-size:14px">NO0010098412</div>
    <div class="card-row abs" style="left:0;top:51px;width:268px"></div>
    <div class="abs" style="left:15px;top:67px;font-size:17px;color:var(--accent)">Cost</div>
    <div class="abs" style="left:15px;top:98px;font-size:11px;color:var(--soft)">Marta Kvistad</div>
    <div class="abs small" style="left:15px;top:128px">Lspende Kostnader</div>
    <div class="card-row abs" style="left:0;top:152px;width:268px"></div>
    <div class="abs small" style="left:15px;top:166px">Lspende Kostnader</div>
    <div class="abs tiny" style="left:15px;top:182px">21.01.2014</div>
    <div class="abs small" style="left:186px;top:166px;color:var(--muted)">1,00%</div>
    <div class="card-row abs" style="left:0;top:206px;width:268px"></div>
    <div class="abs small" style="left:15px;top:226px">Resultabasert avg.</div>
    <div class="abs small" style="left:186px;top:226px;color:var(--muted)">10,00%</div>
  </section>

  <section class="panel abs" style="left:305px;top:766px;width:270px;height:264px">
    <div class="abs card-head" style="left:20px;top:10px">Rating</div>
    <svg class="abs" style="left:94px;top:11px" width="98" height="18" viewBox="0 0 98 18">
      <defs><path id="star" d="M8 1l2 4.7 5 .4-3.8 3.3 1.2 5L8 11.8 3.6 14.4l1.2-5L1 6.1l5-.4z"/></defs>
      <use href="#star" fill="#eceef0"/><use href="#star" x="20" fill="#eceef0"/><use href="#star" x="40" fill="#eceef0"/><use href="#star" x="60" fill="#eceef0"/>
      <use href="#star" x="80" fill="none" stroke="#eceef0" stroke-width="1.1"/>
    </svg>
    <div class="card-row abs" style="left:0;top:51px;width:268px"></div>
    <div class="abs card-head" style="left:20px;top:64px">Risk</div>
    <div class="abs" style="left:20px;top:104px;font-size:13px">Sharp</div>
    <div class="abs" style="left:20px;top:128px;font-size:13px">Avr Return</div>
    <div class="abs" style="left:20px;top:152px;font-size:13px">Std dev</div>
  </section>

  <h2 class="panel-title abs" style="left:596px;top:628px">Performance</h2>
  <table class="perf abs">
    <thead><tr><th></th><th style="border-right:none"></th></tr></thead>
    <tbody>
      <tr><td>1W</td><td>+2,04%</td></tr>
      <tr><td>1M</td><td>+1,05%</td></tr>
      <tr><td>3M</td><td>+3,29%</td></tr>
      <tr><td>6M</td><td>+6,34%</td></tr>
      <tr><td>YTD</td><td>+10,23%</td></tr>
      <tr><td>1Y</td><td>+23,22%</td></tr>
      <tr><td>3Y Ann</td><td>+14,21%</td></tr>
      <tr><td>5Y Ann</td><td>+15,24%</td></tr>
    </tbody>
  </table>

  <footer class="footer abs">Copyright &copy; 2014 Ledgerwise &nbsp; All rights reserved.</footer>
</div>
</body>
</html>
```